BrambleWorks business card

Looking for business card design that supports our company/software values. We have 2 logo designs at the moment but open to change if you think you can enhance the brand. Check out website www.brambleworks.com.au.

Target Market(s)

Education

Contact Information for Business Card

Name, title, mobile, email and website

Font styles to use
Sans Serif

Colors

Designer to choose colors to be used in the design.

Requirements
Must have
• BrambleWorks logo with tree and tagline on rear side with dark grey background colour

```html
<!DOCTYPE html>
<html lang="en">
<head>
<meta charset="utf-8">
<title>BrambleWorks business card</title>
<link href="https://fonts.googleapis.com/css2?family=Ubuntu:wght@400;700&family=Open+Sans:wght@400;700&display=swap" rel="stylesheet">
<style>
  :root {
    --page: #ececec;
    --card: #ffffff;
    --ink: #4f5052;
    --brand-green: #6aa842;
    --deep-green: #2f7a3e;
    --leaf-grey: #a9a7a4;
    --rule: #8a8a8a;
  }
  * { box-sizing: border-box; margin: 0; padding: 0; }
  html, body { width: 1200px; height: 1200px; overflow: hidden; }
  body {
    background: var(--page);
    font-family: "Ubuntu", "Open Sans", sans-serif;
    color: var(--ink);
    position: relative;
  }
  .card {
    position: absolute;
    left: 220px;
    width: 760px;
    height: 430px;
    background: var(--card);
    overflow: hidden;
  }
  .card--front { top: 150px; }
  .card--back { top: 620px; }
  .card__band {
    position: absolute; right: 0; top: 0; bottom: 0;
    width: 20px; background: var(--brand-green);
  }
  .leaf-field {
    position: absolute; left: 0; top: 0; bottom: 0; width: 270px;
  }
  .card--front .leaf-field {
    background: radial-gradient(ellipse at 0% 100%, rgba(47,122,62,.85), rgba(106,168,66,.35) 55%, rgba(255,255,255,0) 80%);
  }
  .card--back .leaf-field {
    background: radial-gradient(ellipse at 0% 100%, rgba(150,148,145,.75), rgba(169,167,164,.3) 55%, rgba(255,255,255,0) 80%);
  }
  .lockup { position: absolute; display: flex; align-items: center; }
  .lockup__dot { border-radius: 50%; background: var(--brand-green); flex: none; }
  .lockup__name { font-weight: 400; color: var(--ink); line-height: 1; white-space: nowrap; }
  .lockup__tagline {
    font-weight: 400; color: var(--ink);
    border-top: 2px solid var(--rule);
    white-space: nowrap;
  }
  .card--front .lockup { left: 300px; top: 158px; gap: 20px; }
  .card--front .lockup__dot { width: 60px; height: 60px; }
  .card--front .lockup__name { font-size: 46px; }
  .card--front .lockup__tagline { font-size: 22px; margin-top: 10px; padding-top: 7px; }

  .card--back .lockup { left: 200px; top: 166px; gap: 16px; }
  .card--back .lockup__dot { width: 44px; height: 44px; }
  .card--back .lockup__name { font-size: 30px; }
  .card--back .lockup__tagline { font-size: 13px; margin-top: 5px; padding-top: 4px; }

  .holder {
    position: absolute; left: 486px; top: 170px;
    border-left: 2px solid var(--rule);
    padding-left: 12px;
    font-family: "Open Sans", sans-serif;
    font-weight: 700; color: var(--deep-green);
    font-size: 24px; line-height: 1.3;
    white-space: nowrap;
  }
  .holder__title { font-size: 20px; }
  .contact {
    position: absolute; right: 38px; bottom: 14px;
    display: flex; gap: 18px; align-items: center;
    font-family: "Open Sans", sans-serif;
    font-size: 12px; color: var(--ink); letter-spacing: .03em;
    white-space: nowrap;
  }
  .contact__item { display: flex; align-items: center; gap: 5px; }
  .contact__icon { width: 16px; height: 16px; fill: var(--ink); }
</style>
</head>
<body>
  <section class="card card--front">
    <div class="leaf-field" role="img" aria-label="Scattered green leaves blowing in from the left edge"></div>
    <div class="lockup">
      <span class="lockup__dot"></span>
      <div>
        <div class="lockup__name">BrambleWorks</div>
        <div class="lockup__tagline">Student Success Platform</div>
      </div>
    </div>
    <div class="card__band"></div>
  </section>

  <section class="card card--back">
    <div class="leaf-field" role="img" aria-label="Scattered grey leaves blowing in from the left edge"></div>
    <div class="lockup">
      <span class="lockup__dot"></span>
      <div>
        <div class="lockup__name">BrambleWorks</div>
        <div class="lockup__tagline">Student Success Platform</div>
      </div>
    </div>
    <div class="holder">
      <div class="holder__name">MARTA VELLOSO</div>
      <div class="holder__title">(NAME)</div>
    </div>
    <div class="contact">
      <span class="contact__item">
        <svg class="contact__icon" viewBox="0 0 16 16"><path d="M4 1l3 3-2 2c1 2 3 4 5 5l2-2 3 3-2 3C7 15 1 9 1 3z"/></svg>
        021 555 014
      </span>
      <span class="contact__item">
        <svg class="contact__icon" viewBox="0 0 16 16"><path d="M1 3h14v10H1z M2 4l6 5 6-5" fill="none" stroke="#4f5052" stroke-width="1.5"/></svg>
        HELLO@BRAMBLEWORKS.COM
      </span>
      <span class="contact__item">
        <svg class="contact__icon" viewBox="0 0 16 16"><g fill="none" stroke="#4f5052" stroke-width="1.3"><circle cx="8" cy="8" r="6.5"/><ellipse cx="8" cy="8" rx="3" ry="6.5"/><path d="M1.5 8h13M2.5 5h11M2.5 11h11"/></g></svg>
        WWW.BRAMBLEWORKS.COM
      </span>
    </div>
    <div class="card__band"></div>
  </section>
</body>
</html>
```